Harbor Nightclub

Nightclub flyer., digital single sided, for KV and PX. I included samples of some previous flyers we've used. Sample Info:
HARBOR
FRIDAYS
FRI MAY 1 2020
DJ VORTAN (club floor)
DJ RUZO & DJ TAV (residents on the lounge floor)
4217 Marlow Avenue Sacramento
www.harborvenuehall.example for list/VIP inquiries

Target Market(s)

Upscale top 40 crowd but want some cool and artsy like the examples included.

Font styles to use
Sans Serif

Requirements
Must have
• Harbor Logo
Nice to have
• Would be nice if the flyer can be incorporated later with DJ photos (sometimes we will add dj photos to pixagram etc). Would like a big city type of feel.
Should not have
• Nothing too sexual.

```html
<!DOCTYPE html>
<html lang="en">
<head>
<meta charset="utf-8">
<title>Harbor Fridays</title>
<link href="https://fonts.googleapis.com/css2?family=Montserrat:wght@200;300;400;500;600;700&display=swap" rel="stylesheet">
<style>
  :root {
    --violet-deep: #1c0c2e;
    --violet-mid: #5a2f85;
    --violet-bright: #9a63d0;
    --lavender: #c39bd6;
    --lavender-text: #b98ccf;
    --brand-purple: #a47cc0;
    --ink: #000000;
    --paper: #ffffff;
  }
  * { margin: 0; padding: 0; box-sizing: border-box; }
  html, body { width: 1200px; height: 629px; overflow: hidden; background: var(--paper); }
  .flyer {
    position: relative;
    width: 1200px;
    height: 629px;
    overflow: hidden;
    font-family: "Montserrat", sans-serif;
    color: var(--paper);
  }
  .backdrop {
    position: absolute; inset: 0;
    background:
      linear-gradient(160deg, rgba(255,255,255,0.12) 0%, transparent 30%),
      linear-gradient(125deg, var(--violet-mid) 0%, var(--violet-deep) 35%, var(--violet-bright) 60%, var(--violet-deep) 85%, var(--violet-mid) 100%);
  }
  .shapes { position: absolute; inset: 0; }
  .title {
    position: absolute;
    left: 150px; top: 26px;
    font-size: 76px; font-weight: 400; letter-spacing: 7px;
    color: var(--brand-purple);
    line-height: 1;
  }
  .subtitle {
    position: absolute;
    left: 150px; top: 124px;
    font-size: 46px; font-weight: 300; letter-spacing: 31px;
    line-height: 1;
  }
  .dj-photo {
    position: absolute;
    width: 111px; height: 105px;
    background: linear-gradient(150deg, #6d6670 0%, #2a262c 60%, #141214 100%);
  }
  .dj-photo--one { left: 37px; top: 217px; }
  .dj-photo--two { left: 37px; top: 355px; background: linear-gradient(150deg, #8a8489 0%, #3a363a 60%, #1a181a 100%); }
  .dj-photo--three { left: 37px; top: 490px; background: linear-gradient(150deg, #a3a0a3 0%, #4a4649 55%, #1e1c1e 100%); }
  .dj-name {
    position: absolute;
    left: 152px;
    font-size: 40px; font-weight: 600; letter-spacing: 2px;
    line-height: 1;
  }
  .dj-name--one { top: 225px; }
  .dj-name--two { top: 364px; }
  .dj-floor {
    position: absolute;
    left: 150px;
    background: var(--ink);
    font-size: 15px; font-weight: 400; letter-spacing: 3px;
    padding: 2px 6px;
    line-height: 1.2;
  }
  .dj-floor--one { top: 277px; }
  .dj-floor--two { top: 415px; }
  .event-date {
    position: absolute;
    left: 612px; top: 293px;
    font-size: 42px; font-weight: 600; letter-spacing: 4px;
    color: var(--lavender-text);
    line-height: 1;
  }
  .event-address {
    position: absolute;
    left: 607px; top: 342px;
    background: var(--ink);
    padding: 2px 6px;
    font-size: 19px; font-weight: 400; letter-spacing: 1.5px;
    line-height: 1.2;
  }
  .contact-mark {
    position: absolute;
    left: 541px; top: 570px;
    width: 36px; height: 36px;
    border-radius: 50%;
    background: var(--lavender);
  }
  .contact-url {
    position: absolute;
    left: 612px; top: 562px;
    font-size: 23px; font-weight: 400; letter-spacing: 2.5px;
    color: var(--lavender-text);
    line-height: 1;
  }
  .contact-url strong { font-weight: 600; }
  .contact-note {
    position: absolute;
    left: 612px; top: 598px;
    font-size: 16px; font-weight: 500; letter-spacing: 1.5px;
    line-height: 1;
  }
</style>
</head>
<body>
<main class="flyer">
  <div class="backdrop" role="img" aria-label="Purple-toned photograph of a modern city building interior with steel beams and lit ceiling panels"></div>

  <svg class="shapes" width="1200" height="629" viewBox="0 0 1200 629" aria-hidden="true">
    <!-- diagonal light bands -->
    <polygon points="560,0 640,0 1200,300 1200,340" fill="var(--paper)" opacity="0.85"/>
    <polygon points="700,0 760,0 1200,230 1200,262" fill="var(--paper)" opacity="0.35"/>
    <polygon points="0,510 40,510 260,629 200,629" fill="var(--paper)" opacity="0.25"/>
    <!-- title bands -->
    <polygon points="0,22 720,22 650,111 0,111" fill="var(--paper)"/>
    <polygon points="0,111 650,111 605,178 0,178" fill="var(--ink)"/>
    <polygon points="620,178 700,178 760,205 680,205" fill="var(--paper)"/>
    <!-- row one -->
    <polygon points="148,217 560,217 520,270 148,270" fill="var(--ink)"/>
    <polygon points="37,270 520,270 640,322 37,322" fill="var(--lavender)"/>
    <!-- date band -->
    <polygon points="600,291 1200,291 1200,339 600,339" fill="var(--ink)"/>
    <!-- row two -->
    <polygon points="148,355 600,355 560,408 148,408" fill="var(--ink)"/>
    <polygon points="37,408 560,408 700,460 37,460" fill="var(--lavender)"/>
    <!-- row three -->
    <polygon points="0,490 560,490 640,530 0,530" fill="var(--lavender)" opacity="0.9"/>
    <!-- contact band -->
    <polygon points="560,553 1200,553 1200,629 520,629" fill="var(--ink)"/>
  </svg>

  <h1 class="title">HARBOR</h1>
  <p class="subtitle">FRIDAYS</p>

  <div class="dj-photo dj-photo--one" role="img" aria-label="Portrait photo of DJ Vortan"></div>
  <h2 class="dj-name dj-name--one">DJ VORTAN</h2>
  <p class="dj-floor dj-floor--one">( CLUB FLOOR )</p>

  <div class="dj-photo dj-photo--two" role="img" aria-label="Portrait photo of DJ Ruzo"></div>
  <h2 class="dj-name dj-name--two">DJ RUZO &amp; DJ TAV</h2>
  <p class="dj-floor dj-floor--two">( RESIDENTS ON THE LOUNGE FLOOR )</p>

  <div class="dj-photo dj-photo--three" role="img" aria-label="Portrait photo of DJ Tav"></div>

  <p class="event-date">FRI MAY 1 2020</p>
  <p class="event-address">4217 MARLOW AVENUE SACRAMENTO</p>

  <span class="contact-mark" aria-hidden="true"></span>
  <p class="contact-url">WWW.<strong>HARBORVENUEHALL</strong>.EXAMPLE</p>
  <p class="contact-note">FOR LIST / VIP INQUIRIES</p>
</main>
</body>
</html>
```